Gemstone Jewelry Online Shop Needs a Banner Design

We need a banner design for a new gemstone Jewelry Online Shop based in the U.S. called "Velanor". One of our selling points is "never fall out of stone". We want to express: a Party Queen doesn't need to worry whenever she may meet an embarrassing moment - a stone of jewelry falls out at a very important occasion. Please insert one of attached images. Please visit our website for more details: http://velanor-shop.example/
The banner size: 1200*628
If you think other images at our website are better, please let us know. Many thanks and looking forward to your beautiful and creative designs!

Industry/Entity Type

Jewelry

```html
<!DOCTYPE html>
<html lang="en">
<head>
<meta charset="utf-8">
<title>Velanor – Never fall out of stone</title>
<link rel="stylesheet" href="https://fonts.googleapis.com/css2?family=EB+Garamond:ital,wght@1,500&family=Lato:wght@400;700&display=swap">
<style>
  :root {
    --cream: #fbf9ee;
    --sun: #fbd977;
    --ink: #1b1b1b;
    --button: #d3d8d8;
    --button-text: #2a2a2a;
    --field-light: #c9c7a2;
    --field-mid: #8c9a5c;
    --field-dark: #4d6b2e;
  }
  html, body {
    margin: 0;
    padding: 0;
    overflow: hidden;
  }
  .banner {
    position: relative;
    width: 1200px;
    height: 628px;
    overflow: hidden;
    background: var(--cream);
    font-family: "Lato", Arial, sans-serif;
    color: var(--ink);
  }
  .model-photo {
    position: absolute;
    left: 0;
    top: 0;
    width: 627px;
    height: 628px;
    background:
      radial-gradient(ellipse 45% 55% at 45% 70%, #dfe6ee 0%, #c7d2de 55%, transparent 75%),
      linear-gradient(100deg, var(--field-light) 0%, var(--field-mid) 40%, var(--field-dark) 70%, var(--field-mid) 100%);
  }
  .brand-band {
    position: absolute;
    left: 627px;
    top: 0;
    width: 573px;
    height: 110px;
    background: var(--sun);
  }
  .brand-name {
    position: absolute;
    left: 0;
    right: 0;
    top: 33px;
    text-align: center;
    font-family: "Lato", Arial, sans-serif;
    font-weight: 700;
    font-size: 40px;
    line-height: 1;
    letter-spacing: 1px;
    color: var(--ink);
  }
  .headline {
    margin: 0;
    font-family: "EB Garamond", Georgia, serif;
    font-style: italic;
    font-weight: 500;
    font-size: 52px;
    line-height: 1;
    color: var(--ink);
  }
  .headline span {
    position: absolute;
    white-space: nowrap;
  }
  .headline .line-1 { left: 649px; top: 158px; }
  .headline .line-2 { left: 711px; top: 204px; }
  .headline .line-3 { left: 791px; top: 244px; }
  .slogan {
    margin: 0;
    font-weight: 700;
    font-size: 54px;
    line-height: 1;
    letter-spacing: 1px;
    color: var(--ink);
  }
  .slogan span {
    position: absolute;
    white-space: nowrap;
  }
  .slogan .line-1 { left: 660px; top: 326px; }
  .slogan .line-2 { left: 689px; top: 376px; }
  .pendant-photo {
    position: absolute;
    left: 1012px;
    top: 268px;
    width: 188px;
    height: 212px;
    background:
      radial-gradient(circle at 55% 55%, #c9304f 0%, #e59a3a 30%, #d7dbe0 58%, transparent 75%);
  }
  .shop-button {
    position: absolute;
    left: 767px;
    top: 516px;
    width: 296px;
    height: 60px;
    background: var(--button);
    color: var(--button-text);
    font-size: 31px;
    font-weight: 400;
    letter-spacing: 0.5px;
    text-align: center;
    line-height: 60px;
    text-decoration: none;
  }
</style>
</head>
<body>
  <main class="banner">
    <div class="model-photo" role="img" aria-label="Photo of a young woman in a light blue lace blouse wearing a flower earring and ring, in a field of tall pampas grass"></div>

    <header class="brand-band">
      <div class="brand-name">Velanor</div>
    </header>

    <h1 class="headline">
      <span class="line-1">Don’t worry about</span>
      <span class="line-2">that embarrassing</span>
      <span class="line-3">moment</span>
    </h1>

    <p class="slogan">
      <span class="line-1">“Never fall</span>
      <span class="line-2">out of stone”</span>
    </p>

    <div class="pendant-photo" role="img" aria-label="Silver butterfly pendant necklace set with garnet, citrine, pink and green gemstones"></div>

    <a class="shop-button" href="http://velanor-shop.example/">SHOP NOW</a>
  </main>
</body>
</html>
```